I need a Label design for my copper 71 kombucha brand that is launching soon

I want a label to go on my copper 71 kombucha bottle.
I have a logo image uploaded in the files but I am open to changes to this logo or even a completely New one if you think you can do better. This logo is based on the idea of an s-shaped naga. I particularly like the nagas from temples in luang prabang.
I also want to include the slogan - Sip bold, stay bright.
The label should be some kind of oval at 80mm high by 70mm wide.
The label will go on a clear glass bottle. The kombucha will be visible and comes in different shades of red,yellow and purple.
The word kombucha should be clearly visible.
i want a very colorful, playful label. I'm very keen to see your ideas and I want something original.
Fermented foods and beverages

```html
<!DOCTYPE html>
<html lang="en">
<head>
<meta charset="utf-8">
<title>copper 71 Kombucha Label</title>
<link href="https://fonts.googleapis.com/css2?family=Comfortaa:wght@700&family=Lilita+One&display=swap" rel="stylesheet">
<style>
  :root {
    --backdrop: #e6e6e6;
    --label-orange: #df8a24;
    --label-orange-light: #eaa23a;
    --label-orange-deep: #d27a1c;
    --ring-gold: #f1c72a;
    --blob-red: #bf1c1f;
    --blob-bright-red: #e40a0a;
    --blob-maroon: #7c1738;
    --blob-yellow: #edb245;
    --dot-blush: #f5dcd3;
    --text-white: #ffffff;
    --text-cream: #fdf1e4;
  }
  html, body {
    margin: 0;
    padding: 0;
    width: 1200px;
    height: 1200px;
    overflow: hidden;
    background: var(--backdrop);
  }
  .label-canvas {
    display: block;
    width: 1200px;
    height: 1200px;
  }
  .brand-name {
    font-family: "Comfortaa", sans-serif;
    font-weight: 700;
    font-size: 62px;
    fill: var(--text-white);
  }
  .product-title {
    font-family: "Lilita One", sans-serif;
    font-size: 150px;
    fill: var(--text-white);
  }
  .slogan {
    font-family: "Comfortaa", sans-serif;
    font-weight: 700;
    font-size: 37px;
    fill: var(--text-cream);
  }
</style>
</head>
<body>
<svg class="label-canvas" viewBox="0 0 1200 1200" xmlns="http://www.w3.org/2000/svg">
  <defs>
    <clipPath id="label-shape">
      <ellipse cx="600" cy="600" rx="380" ry="435"/>
    </clipPath>
    <radialGradient id="label-glow" cx="50%" cy="48%" r="60%">
      <stop offset="0%" stop-color="var(--label-orange-light)"/>
      <stop offset="60%" stop-color="var(--label-orange)"/>
      <stop offset="100%" stop-color="var(--label-orange-deep)"/>
    </radialGradient>
  </defs>

  <g class="oval-label" clip-path="url(#label-shape)">
    <rect class="label-background" x="200" y="150" width="800" height="900" fill="url(#label-glow)"
          role="img" aria-label="Orange sunburst background"/>

    <g class="decorative-blobs" role="img" aria-label="Playful red, maroon and yellow organic shapes with leaves">
      <ellipse cx="494" cy="232" rx="120" ry="72" fill="var(--blob-yellow)"/>
      <ellipse cx="290" cy="482" rx="95" ry="140" transform="rotate(15 290 482)" fill="var(--blob-maroon)"/>
      <ellipse cx="872" cy="419" rx="110" ry="205" transform="rotate(-22 872 419)" fill="var(--blob-red)"/>
      <ellipse cx="360" cy="865" rx="112" ry="125" transform="rotate(-25 360 865)" fill="var(--blob-bright-red)"/>
      <ellipse cx="815" cy="908" rx="125" ry="82" transform="rotate(-15 815 908)" fill="var(--blob-yellow)"/>
    </g>

    <circle class="accent-dot" cx="529" cy="861" r="28" fill="var(--dot-blush)"/>
    <circle class="accent-dot" cx="695" cy="858" r="17" fill="var(--dot-blush)"/>
  </g>

  <ellipse class="gold-ring" cx="600" cy="600" rx="348" ry="403" fill="none" stroke="var(--ring-gold)" stroke-width="4"/>

  <circle class="brand-mark" cx="600" cy="386" r="72" fill="none" stroke="var(--text-white)" stroke-width="10"/>
  <text class="brand-name" x="600" y="545" text-anchor="middle">copper 71</text>
  <text class="product-title" x="600" y="731" text-anchor="middle" textLength="520" lengthAdjust="spacingAndGlyphs">KOMBUCHA</text>
  <text class="slogan" x="600" y="775" text-anchor="middle" textLength="375" lengthAdjust="spacingAndGlyphs">Sip bold, stay bright</text>
</svg>
</body>
</html>
```